Modern Label for Loose Tea pouches on 4.5x6 Label

We need a new label for our teas that is very simple in design, but stylish and modern. This will be used to print labels for our loose tea pouches. The label will be at max 4.5x6 inches in size. There should be a place for the tea name, description, ingredients, and size that is changeable.
Preferably an AI file that allows me to setup variables to change the above items. There will also need to be our logo which is supplied, and our address on the label.
Address:
Tessaly Leaf
846 Lower Maple Lane
Larkhaven, VT 05917
Target Market(s)
Tea Lovers
Requirements
Must have
- Adobe Illustrator file with variables setup for replacement of tea name, description, ingredients, and size (weights 2oz, 4oz, 8oz, 1lb)

```html
<!DOCTYPE html>
<html lang="en">
<head>
<meta charset="UTF-8">
<title>Tessaly Leaf – Loose Tea Label</title>
<link rel="stylesheet" href="https://fonts.googleapis.com/css2?family=Source+Sans+3:wght@400;600;700&display=swap">
<style>
  :root {
    --bg-deep: #1c0305;
    --wood-warm: #6a3a22;
    --wood-dark: #3a1810;
    --tea-amber: #b4501c;
    --tea-glow: #e2a02a;
    --brand-green: #b6d02f;
    --brand-pink: #d94f9c;
    --text-light: #ffffff;
    --badge-bg: #ffffff;
    --badge-ink: #3a0508;
  }
  * { margin: 0; padding: 0; box-sizing: border-box; }
  html, body { width: 900px; height: 1200px; overflow: hidden; background: var(--bg-deep); }
  .label {
    position: relative;
    width: 900px;
    height: 1200px;
    overflow: hidden;
    background: var(--bg-deep);
    font-family: "Source Sans 3", "Myriad Pro", sans-serif;
    color: var(--text-light);
  }
  .hero-photo {
    position: absolute;
    left: 0; top: 380px;
    width: 900px; height: 640px;
    background:
      radial-gradient(ellipse 260px 170px at 200px 450px, var(--tea-glow) 0%, var(--tea-amber) 40%, rgba(120,40,15,0) 100%),
      radial-gradient(ellipse 520px 300px at 330px 280px, var(--wood-warm) 0%, var(--wood-dark) 60%, rgba(28,3,5,0) 100%),
      linear-gradient(to bottom, var(--bg-deep) 0%, rgba(28,3,5,0) 18%, rgba(28,3,5,0) 80%, var(--bg-deep) 100%);
  }
  .brand-mark {
    position: absolute;
    left: 395px; top: 100px;
    width: 110px; height: 110px;
    border-radius: 50%;
    background: var(--brand-pink);
  }
  .brand-name {
    position: absolute;
    left: 0; top: 306px;
    width: 900px;
    text-align: center;
    font-size: 80px;
    font-weight: 700;
    letter-spacing: 2px;
    line-height: 1;
    color: var(--brand-green);
  }
  .section-title {
    font-size: 33px;
    font-weight: 400;
    line-height: 1.2;
  }
  .description {
    position: absolute;
    left: 0; top: 438px;
    width: 900px;
    text-align: center;
  }
  .description p {
    font-size: 21.5px;
    line-height: 26.7px;
  }
  .ingredients {
    position: absolute;
    left: 553px; top: 634px;
    width: 312px;
  }
  .ingredients p {
    font-size: 21.5px;
    line-height: 26.7px;
    text-align: justify;
  }
  .address {
    position: absolute;
    left: 46px; top: 1036px;
    font-size: 25px;
    line-height: 31.4px;
    font-style: normal;
  }
  .weight-badge {
    position: absolute;
    left: 686px; top: 1060px;
    width: 300px; height: 300px;
    border-radius: 50%;
    background: var(--badge-bg);
    color: var(--badge-ink);
  }
  .weight-label {
    position: absolute;
    left: 0; top: 20px;
    width: 228px;
    text-align: center;
    font-size: 31px;
    font-weight: 700;
  }
  .weight-value {
    position: absolute;
    left: 0; top: 50px;
    width: 228px;
    text-align: center;
    font-size: 66px;
    font-weight: 400;
    line-height: 1.2;
  }
</style>
</head>
<body>
  <main class="label">
    <div class="hero-photo" role="img" aria-label="Photo of a steaming glass cup of amber tea on a saucer with mint leaves, set against a warm wooden backdrop"></div>

    <header class="brand">
      <span class="brand-mark" aria-hidden="true"></span>
      <h1 class="brand-name">TESSALY LEAF</h1>
    </header>

    <section class="description">
      <h2 class="section-title">Description</h2>
      <p>Lorem ipsum dolor sit amet, consectetuer adipiscing elit.<br>
      Aenean commodo ligula eget dolor.<br>
      Aenean massa</p>
    </section>

    <section class="ingredients">
      <h2 class="section-title">Ingredients:</h2>
      <p>Lorem ipsum dolor sit amet, consectetuer adipiscing elit. Aenean commodo ligula eget dolor. Aenean massa. Cum sociis natoque penatibus et magnis dis parturient montes, nascetur ridiculus mus. Donec quam felis, ultricies nec, pellentesque eu, pretium quis, sem.</p>
    </section>

    <address class="address">
      Address:<br>
      Tessaly Leaf<br>
      846 Lower Maple Lane<br>
      Larkhaven, VT 05917
    </address>

    <div class="weight-badge">
      <span class="weight-label">weights</span>
      <span class="weight-value">2oz</span>
    </div>
  </main>
</body>
</html>
```